Business card for law firm

Need business card for new law firm. Think confident, authoritative, conservative, but not stuffy or old-fashioned.

Contact Information for Business Card

Content for card - logo (uploaded), plus the following:

Paul Wexbury (larger font)
Managing Partner (larger font, but not as large as name)
Level 9, 41 Tansy Lane
Sydney NSW 2000
Main Tel 02 7346 2190
Direct Tel 02 6273 4415
Email paul@qvlegal.com.au
www.qvlegal.com.au

Letterhead design should include logo plus:
Level 9, 41 Tansy Lane
Sydney NSW 2000
Tel 02 6273 4415
www.qvlegal.com.au

```html
<!DOCTYPE html>
<html lang="en">
<head>
<meta charset="utf-8">
<title>Quillvale Legal – Business Card</title>
<link rel="stylesheet" href="https://fonts.googleapis.com/css2?family=Libre+Baskerville:wght@400;700&family=Montserrat:wght@400;500&display=swap">
<style>
  :root {
    --navy: #2e3659;
    --navy-deep: #262d4c;
    --paper: #f7f7f6;
    --backdrop: #ececec;
    --ink: #3a3a3a;
    --rule: #b9b9b9;
    --white: #ffffff;
  }
  * { box-sizing: border-box; margin: 0; padding: 0; }
  html, body {
    width: 1200px; height: 1108px; overflow: hidden;
    background: var(--backdrop);
  }
  .canvas { position: relative; width: 1200px; height: 1108px; }

  .card {
    position: absolute;
    width: 660px; height: 378px;
    box-shadow: 0 10px 28px rgba(0,0,0,0.12), 0 2px 6px rgba(0,0,0,0.08);
  }

  /* Back of card */
  .card-back {
    left: 460px; top: 110px;
    background: var(--navy);
    display: flex; align-items: center; justify-content: center;
  }

  /* Wordmark */
  .wordmark {
    display: flex; align-items: center; gap: 18px;
    font-family: "Libre Baskerville", serif;
    font-weight: 400;
  }
  .wordmark-square { width: 34px; height: 34px; flex: none; }
  .wordmark-text { display: flex; flex-direction: column; line-height: 1; }
  .wordmark-name { letter-spacing: 0.04em; text-transform: uppercase; }
  .wordmark-sub { letter-spacing: 0.62em; text-transform: uppercase; margin-top: 10px; }

  .card-back .wordmark { color: var(--white); }
  .card-back .wordmark-square { background: var(--white); width: 46px; height: 46px; }
  .card-back .wordmark-name { font-size: 50px; }
  .card-back .wordmark-sub { font-size: 13px; margin-left: 6px; }

  /* Front of card */
  .card-front {
    left: 80px; top: 620px;
    background: var(--paper);
  }
  .card-front-body {
    position: absolute; left: 0; top: 0; right: 0; height: 328px;
    display: flex; align-items: center;
  }
  .brand-panel {
    width: 330px; display: flex; justify-content: center;
  }
  .card-front .wordmark { color: var(--ink); gap: 14px; }
  .card-front .wordmark-square { background: var(--navy); }
  .card-front .wordmark-name { font-size: 30px; }
  .card-front .wordmark-sub { font-size: 9px; margin-top: 8px; }

  .divider { width: 1px; height: 150px; background: var(--rule); }

  .contact-panel {
    flex: 1; padding-left: 30px;
    font-family: "Montserrat", sans-serif;
    color: var(--ink);
  }
  .person-name {
    font-family: "Libre Baskerville", serif;
    font-weight: 700; font-size: 24px; color: var(--navy);
  }
  .person-role { font-size: 14px; margin-top: 4px; }
  .address { font-size: 13px; line-height: 1.45; margin-top: 12px; }
  .contact-list { list-style: none; margin-top: 10px; font-size: 13px; line-height: 1.55; }
  .contact-list li { display: flex; align-items: center; gap: 9px; }
  .contact-list svg { width: 12px; height: 12px; flex: none; }

  .card-front-band {
    position: absolute; left: 0; right: 0; bottom: 0; height: 50px;
    background: var(--navy);
    border-top: 3px solid var(--paper);
    box-shadow: 0 -1px 0 var(--navy-deep);
  }
</style>
</head>
<body>
<main class="canvas">

  <section class="card card-back" aria-label="Back of business card">
    <div class="wordmark">
      <span class="wordmark-square" aria-hidden="true"></span>
      <span class="wordmark-text">
        <span class="wordmark-name">Quillvale</span>
        <span class="wordmark-sub">Legal</span>
      </span>
    </div>
  </section>

  <section class="card card-front" aria-label="Front of business card">
    <div class="card-front-body">
      <div class="brand-panel">
        <div class="wordmark">
          <span class="wordmark-square" aria-hidden="true"></span>
          <span class="wordmark-text">
            <span class="wordmark-name">Quillvale</span>
            <span class="wordmark-sub">Legal</span>
          </span>
        </div>
      </div>
      <div class="divider"></div>
      <div class="contact-panel">
        <p class="person-name">Paul Wexbury</p>
        <p class="person-role">Managing Partner</p>
        <p class="address">Level 9, 41 Tansy Lane<br>Sydney NSW 2000</p>
        <ul class="contact-list">
          <li>
            <svg viewBox="0 0 12 12" aria-hidden="true"><path d="M3 1 L4.6 3.4 L3.6 4.6 Q4.6 6.8 7.4 8.4 L8.6 7.4 L11 9 L9.8 11 Q4.5 10.5 1 3 Z" fill="#3a3a3a"/></svg>
            02 7346 2190 (Main)
          </li>
          <li>
            <svg viewBox="0 0 12 12" aria-hidden="true"><path d="M3 1 L4.6 3.4 L3.6 4.6 Q4.6 6.8 7.4 8.4 L8.6 7.4 L11 9 L9.8 11 Q4.5 10.5 1 3 Z" fill="#3a3a3a"/></svg>
            02 6273 4415
          </li>
          <li>
            <svg viewBox="0 0 12 12" aria-hidden="true"><rect x="0.6" y="2.4" width="10.8" height="7.4" fill="none" stroke="#3a3a3a" stroke-width="1"/><path d="M0.8 2.8 L6 6.8 L11.2 2.8" fill="none" stroke="#3a3a3a" stroke-width="1"/></svg>
            paul@qvlegal.com.au
          </li>
          <li>
            <svg viewBox="0 0 12 12" aria-hidden="true"><g fill="none" stroke="#3a3a3a" stroke-width="0.9"><circle cx="6" cy="6" r="5.2"/><ellipse cx="6" cy="6" rx="2.3" ry="5.2"/><path d="M0.8 6 H11.2 M1.6 3.4 H10.4 M1.6 8.6 H10.4"/></g></svg>
            www.qvlegal.com.au
          </li>
        </ul>
      </div>
    </div>
    <div class="card-front-band"></div>
  </section>

</main>
</body>
</html>
```